Univ of Brackenfield disability insurance program

We are an endorsed vendor for disability insurance the the University of Brackenfield. We work together with the University to promote this program. They send emails on our behalf but we send some too. I'm not confident the emails we send are as effective as they could be. I have attached examples of 2 versions of the same email we send students and residents. I would love your opinion on how to make these better and shorter. They are emails, not brochures. I have several others but starting with these. I would like to see consistency in all the pieces we email to the students and residents. I also feel like we have to many words in our pieces and they could be shortened up with better word smithing. Once we settle on a design of these emails and better wording I have about 5 other emails I would like to have looked at to coordinate with the one we are doing now. In each of these programs at the University we have an assigned Penrow Adali representative. We do want to add their pictures to these too as one of the examples has.
Updates

I forgot to mention that I need both logo's in the email. The Penrow Adali logo and the University of Brackenfield Office of Student Health Benefits logo. Do you need an electronic version of the email? Let me know. Thanks

Target Market(s)

students and medical residents

Industry/Entity Type

Insurance

Font styles to use
Sans Serif

Requirements
Must have
• Short and worded to the point
• Can use maroon and gold coloring
Nice to have
• Easier to read
Should not have
• Walls of words as students and residents dont have a lot of extra time on their hands.

```html
<!DOCTYPE html>
<html lang="en">
<head>
<meta charset="utf-8">
<title>Penrow Adali – Attention: Completing Students</title>
<link href="https://fonts.googleapis.com/css2?family=Lato:wght@400;700;900&display=swap" rel="stylesheet">
<style>
  :root {
    --stage: #1b1d22;
    --paper: #ffffff;
    --navy: #1d2a63;
    --band: #8c8c8c;
    --band-dark: #6f6f6f;
    --link-ink: #3a3a3a;
    --rule: #d5d5d5;
    --photo-light: #eef3f7;
    --photo-mid: #b9d3e6;
    --photo-deep: #6f9fc6;
    --portrait: #a9b4bf;
  }
  * { margin: 0; padding: 0; box-sizing: border-box; }
  html, body {
    width: 1200px; height: 848px; overflow: hidden;
    background: var(--stage);
    font-family: 'Lato', sans-serif;
  }
  .canvas {
    width: 1200px; height: 848px;
    display: flex; align-items: center; justify-content: center;
  }
  .flyer {
    position: relative;
    width: 620px; height: 808px;
    background: var(--paper);
    overflow: hidden;
  }
  .hero {
    position: absolute; left: 0; top: 0;
    width: 620px; height: 430px;
  }
  .brand {
    position: absolute; top: 24px; right: 32px;
    display: flex; align-items: center; gap: 10px;
  }
  .brand-mark {
    width: 34px; height: 34px; border-radius: 50%;
    background: var(--navy);
  }
  .brand-name {
    font-size: 24px; font-weight: 700; color: var(--navy);
    letter-spacing: 0.5px;
  }
  .headline {
    position: absolute; left: 30px; right: 20px; top: 400px;
    color: var(--navy);
    font-weight: 900; line-height: 1;
  }
  .headline-main { display: block; font-size: 92px; letter-spacing: 1px; }
  .headline-sub { display: block; font-size: 42px; margin-top: 4px; letter-spacing: 0.5px; }
  .message-band {
    position: absolute; left: 0; right: 0; top: 556px; height: 142px;
    background: var(--band);
    padding: 16px 40px 0;
    color: #fff;
  }
  .message-title { font-size: 30px; font-weight: 400; letter-spacing: 1px; }
  .message-body { font-size: 17px; line-height: 1.3; margin-top: 6px; }
  .message-link { font-size: 17px; font-weight: 700; color: var(--link-ink); margin-top: 8px; }
  .contact-band {
    position: absolute; left: 0; right: 0; top: 708px; bottom: 0;
    background: var(--band-dark);
    display: flex; align-items: center; gap: 16px;
    padding: 0 24px;
    color: #fff;
  }
  .rep-photo {
    flex: none; width: 70px; height: 70px; border-radius: 50%;
    background: var(--portrait);
  }
  .contact-text { display: flex; flex-direction: column; gap: 8px; }
  .contact-title { font-size: 17px; font-weight: 700; }
  .partner {
    display: flex; align-items: center; gap: 8px;
    font-size: 13px; font-weight: 400;
  }
  .partner-mark { width: 12px; height: 12px; background: #fff; }
</style>
</head>
<body>
<main class="canvas">
  <article class="flyer">
    <svg class="hero" viewBox="0 0 620 430" xmlns="http://www.w3.org/2000/svg">
      <defs>
        <linearGradient id="photoTone" x1="0" y1="0" x2="1" y2="1">
          <stop offset="0" stop-color="var(--photo-light)"/>
          <stop offset="0.55" stop-color="var(--photo-mid)"/>
          <stop offset="1" stop-color="var(--photo-deep)"/>
        </linearGradient>
      </defs>
      <g role="img" aria-label="Photo of a smiling young doctor in a white coat with a stethoscope, colleagues reviewing an x-ray behind him">
        <rect x="0" y="0" width="620" height="430" fill="url(#photoTone)"/>
      </g>
      <path d="M0 270 C 140 270, 210 395, 360 395 C 470 395, 540 360, 620 335 L620 430 L0 430 Z" fill="var(--rule)"/>
      <path d="M0 282 C 140 282, 210 407, 360 407 C 470 407, 540 372, 620 347 L620 430 L0 430 Z" fill="var(--paper)"/>
    </svg>

    <header class="brand">
      <span class="brand-mark"></span>
      <span class="brand-name">Penrow Adali</span>
    </header>

    <h1 class="headline">
      <span class="headline-main">ATTENTION:</span>
      <span class="headline-sub">COMPLETING STUDENTS</span>
    </h1>

    <section class="message-band">
      <p class="message-title">FINALLY. IT'S YOUR TIME.</p>
      <p class="message-body">You're close to reaping the rewards of all the hard work and sacrifices you've made to get where you are now.</p>
      <p class="message-link">www.penrowadali.com/jordan-vale</p>
    </section>

    <footer class="contact-band">
      <div class="rep-photo" role="img" aria-label="Portrait photo of the assigned Penrow Adali representative"></div>
      <div class="contact-text">
        <p class="contact-title">Contact your University-Designated Representative</p>
        <p class="partner"><span class="partner-mark"></span>University of Brackenfield Office of Student Health Benefits</p>
      </div>
    </footer>
  </article>
</main>
</body>
</html>
```